Molenvaart

2 homepage design for my tire webshop. One for the winter and one for the summer.
2 items have to come back.
1 a filterbox option to choose tire width, height and inch
2 an option where i can sell my tire mounting service
The customer can buy tires from me but also have the option to use only my skills for mounting their own tire.
My sellingpoint is my mobile service, a webshop with his own mechanic, and my good reputation.

```html
<!DOCTYPE html>
<html lang="en">
<head>
<meta charset="utf-8">
<title>Molenvaart – Winter Tires</title>
<link rel="stylesheet" href="https://fonts.googleapis.com/css2?family=Bebas+Neue&family=Oswald:wght@500;600&family=Roboto:wght@400;500;700&family=Montserrat:wght@400;500;600&display=swap">
<style>
:root{
  --red:#e0262b;
  --black:#111;
  --ink:#222;
  --light-grey:#f0f0f0;
  --navy:#0c0f1e;
  --gold:#f2b01e;
  --white:#fff;
  --muted:#b9b9b9;
}
*{box-sizing:border-box;margin:0;padding:0}
html,body{width:1200px;height:4234px;overflow:hidden}
body{font-family:"Roboto",sans-serif;color:var(--ink);background:var(--white);position:relative}
.heading{font-family:"Bebas Neue",sans-serif;font-weight:400;letter-spacing:.5px}

.alert-bar{position:absolute;top:0;left:0;width:1200px;height:36px;background:var(--black);color:var(--white);font:500 13px "Montserrat",sans-serif;display:flex;align-items:center;justify-content:center;gap:5px}
.alert-bar a{color:var(--white);text-decoration:underline}

.site-nav{position:absolute;top:36px;left:0;width:1200px;height:59px;background:var(--white)}
.logo{position:absolute;left:100px;top:8px;font:400 42px/44px "Bebas Neue",sans-serif;color:var(--black);display:flex;align-items:center;gap:8px}
.logo .mark{width:22px;height:22px;border-radius:50%;background:var(--black)}
.nav-links{position:absolute;left:327px;top:0;height:59px;display:flex;align-items:center;gap:38px;font:500 14px "Montserrat",sans-serif;color:var(--black)}
.call-box{position:absolute;right:0;top:0;width:310px;height:59px;background:var(--red);clip-path:polygon(24px 0,100% 0,100% 100%,0 100%);color:var(--white)}
.call-box svg{position:absolute;left:40px;top:16px}
.call-box .small{position:absolute;left:78px;top:11px;font:600 11px "Montserrat",sans-serif}
.call-box .num{position:absolute;left:78px;top:24px;font:700 20px "Montserrat",sans-serif}

.hero{position:absolute;top:95px;left:0;width:1200px;height:567px;background:linear-gradient(180deg,#4d5865 0%,#37414d 50%,#1a2029 100%)}
.hero-arrow{position:absolute;top:270px;color:var(--white);font:300 34px "Roboto",sans-serif}
.hero-kicker{position:absolute;top:318px;width:1200px;text-align:center;color:var(--white);font:500 22px "Roboto",sans-serif}
.hero-title{position:absolute;top:348px;width:1200px;text-align:center;color:var(--white);font:400 84px/84px "Bebas Neue",sans-serif}
.hero-sub{position:absolute;top:436px;width:1200px;text-align:center;color:var(--white);font:500 23px "Roboto",sans-serif}
.filter-row{position:absolute;top:477px;left:122px;display:flex;gap:7px}
.filter-select{width:199px;height:36px;background:var(--white);border-radius:2px;font:400 12px "Roboto",sans-serif;color:#555;padding:0 14px;display:flex;align-items:center;justify-content:space-between}
.filter-select:after{content:"";border:5px solid transparent;border-top:6px solid #222;margin-top:5px}
.filter-btn{width:130px;height:36px;margin-left:1px;background:var(--red);color:var(--white);font:700 14px "Roboto",sans-serif;display:flex;align-items:center;justify-content:center}

.categories{position:absolute;top:662px;left:0;width:1200px;height:188px;background:var(--white)}
.categories h2{position:absolute;top:28px;width:1200px;text-align:center;font:500 22px "Oswald",sans-serif;color:var(--black)}
.cat{position:absolute;top:80px;width:110px;margin-left:-55px;text-align:center;font:400 12px "Roboto",sans-serif;color:#555}
.cat svg{display:block;margin:0 auto 4px}

.products{position:absolute;top:850px;left:0;width:1200px;height:884px;background:var(--light-grey)}
.products h2{position:absolute;top:73px;width:1200px;text-align:center;font-size:50px;color:var(--black)}
.products .lead{position:absolute;top:130px;width:1200px;text-align:center;font:400 16px "Roboto",sans-serif;color:#333}
.product-card{position:absolute;width:240px;height:309px;background:var(--white);text-align:center}
.product-card .product-photo{width:110px;height:152px;margin:16px auto 0;background:linear-gradient(180deg,#4a4a4a,#2a2a2a)}
.product-card .rating{margin-top:10px;font:400 11px "Roboto",sans-serif;color:#333}
.product-card .rating span{color:var(--gold);letter-spacing:1px;font-size:12px}
.product-card .name{margin-top:4px;font:500 16px "Roboto",sans-serif;color:var(--black)}
.product-card .price{margin-top:10px;font:500 15px "Roboto",sans-serif;color:var(--black)}
.product-card .btn{width:147px;height:36px;margin:10px auto 0;border:1px solid #444;font:500 14px/34px "Roboto",sans-serif;color:var(--black)}

.features{position:absolute;top:1734px;left:0;width:1200px;height:559px;background:var(--white);overflow:hidden}
.features .dark-panel{position:absolute;inset:0;background:var(--navy);clip-path:polygon(468px 0,1200px 0,1200px 559px,608px 559px,468px 430px)}
.features h2{position:absolute;left:101px;top:48px;font:500 22px "Oswald",sans-serif;color:var(--black)}
.feature{position:absolute;left:101px;width:230px}
.feature h3{font:500 18px "Oswald",sans-serif;color:#999}
.feature p{margin-top:6px;font:400 11px/17px "Roboto",sans-serif;color:var(--muted)}
.feature.active{padding-left:16px;border-left:3px solid var(--red)}
.feature.active h3{color:var(--black);font:500 17px "Roboto",sans-serif}
.feature.active p{color:#444}
.feature-visual{position:absolute;left:390px;top:100px;width:322px;height:415px;background:linear-gradient(90deg,#8a8d92 0%,#4a4d52 40%,#7a1e22 75%,#3a1518 100%)}
.rib-label{position:absolute;left:843px;width:230px;color:var(--white)}
.rib-label h4{font:500 14px "Oswald",sans-serif;color:var(--red);padding-bottom:5px;border-bottom:1px solid #cfd3dc}
.rib-label p{margin-top:10px;font:400 11px/17px "Roboto",sans-serif}
.pointer{position:absolute;height:1px;background:#cfd3dc}
.dot{position:absolute;width:14px;height:14px;border-radius:50%;background:rgba(255,255,255,.7);border:2px solid var(--white)}

.mounting{position:absolute;top:2293px;left:0;width:1200px;height:567px;background:linear-gradient(90deg,#5b6570 0%,#4d5762 45%,#2e353e 60%,#454c55 100%)}
.mounting .photo{position:absolute;left:0;top:0;width:620px;height:567px;background:linear-gradient(90deg,#5b6570,#7d8791 60%,rgba(90,100,110,0))}
.mounting h2{position:absolute;left:636px;top:76px;font-size:46px;color:var(--white)}
.mounting .lead{position:absolute;left:636px;top:132px;width:440px;font:400 15px/24px "Roboto",sans-serif;color:var(--white)}
.service{position:absolute;width:215px;color:var(--white)}
.service h3{margin-top:6px;font:500 14px "Roboto",sans-serif}
.service p{margin-top:6px;font:400 10px/19px "Roboto",sans-serif;color:#e4e4e4}
.btn-red{position:absolute;left:636px;top:444px;width:148px;height:36px;background:var(--red);color:var(--white);font:500 15px/36px "Roboto",sans-serif;text-align:center}

.blog{position:absolute;top:2860px;left:0;width:1200px;height:633px;background:var(--white)}
.blog h2{position:absolute;top:84px;width:1200px;text-align:center;font-size:48px;color:var(--black)}
.post{position:absolute;top:157px;width:313px;height:375px;background:var(--white);box-shadow:0 0 6px rgba(0,0,0,.12)}
.post .post-photo{height:190px}
.post h3{margin:14px 16px 0;font:500 21px/26px "Roboto",sans-serif;color:var(--black)}
.post p{margin:10px 18px 0;font:400 13px/26px "Roboto",sans-serif;color:#444}
.post a{display:block;margin:6px 18px 0;font:400 12px "Roboto",sans-serif;color:var(--red);text-decoration:none}

.newsletter{position:absolute;top:3493px;left:0;width:1200px;height:395px;background:linear-gradient(90deg,#55626e 0%,#3b4652 40%,#2a3440 100%)}
.newsletter h2{position:absolute;left:603px;top:100px;font-size:60px;color:var(--white)}
.newsletter .lead{position:absolute;left:603px;top:174px;width:500px;font:400 16px/23px "Roboto",sans-serif;color:var(--white)}
.subscribe{position:absolute;left:603px;top:236px;width:480px;height:42px;background:var(--white);border-radius:21px;overflow:hidden}
.subscribe span{position:absolute;left:15px;top:14px;font:400 12px "Roboto",sans-serif;color:#444}
.subscribe b{position:absolute;right:0;top:0;width:131px;height:42px;border-radius:21px;background:var(--red);color:var(--white);font:700 14px/42px "Roboto",sans-serif;text-align:center}

.site-footer{position:absolute;top:3888px;left:0;width:1200px;height:346px;background:var(--black);color:var(--white)}
.footer-logo{position:absolute;left:100px;top:75px;font:400 58px/60px "Bebas Neue",sans-serif;color:var(--white);display:flex;align-items:center;gap:10px}
.footer-logo .mark{width:28px;height:28px;border-radius:50%;background:var(--white)}
.footer-about{position:absolute;left:100px;top:163px;width:300px;font:400 11px/21px "Roboto",sans-serif}
.footer-col{position:absolute;top:66px}
.footer-col h4{font:500 18px "Montserrat",sans-serif}
.footer-col ul{list-style:none;margin-top:18px}
.footer-col li{font:400 13px "Montserrat",sans-serif;margin-bottom:21px;display:flex;gap:8px;align-items:flex-start}
.social li{align-items:center;margin-bottom:12px;font-size:14px}
.social .ring{width:28px;height:28px;border:2px solid var(--white);border-radius:50%;flex:none}
.footer-rule{position:absolute;left:100px;top:288px;width:1000px;height:1px;background:#333}
.copyright{position:absolute;top:310px;width:1200px;text-align:center;font:400 13px "Roboto",sans-serif}
</style>
</head>
<body>

<div class="alert-bar">CORONAVIRUS (COVID -19) ALERTS <a>Click here for the latest updates</a></div>

<header class="site-nav">
  <div class="logo">MOLENVAART<span class="mark"></span></div>
  <nav class="nav-links"><span>SHOP TIRES</span><span>ABOUT US</span><span>PROMOTIONS</span><span>TIRE FINDER</span><span>SEARCH</span></nav>
  <div class="call-box">
    <svg width="28" height="28" viewBox="0 0 24 24" fill="#fff"><path d="M6.6 10.8a15.1 15.1 0 0 0 6.6 6.6l2.2-2.2a1 1 0 0 1 1-.25 11.4 11.4 0 0 0 3.6.6 1 1 0 0 1 1 1V20a1 1 0 0 1-1 1A17 17 0 0 1 3 4a1 1 0 0 1 1-1h3.5a1 1 0 0 1 1 1c0 1.25.2 2.45.6 3.6a1 1 0 0 1-.25 1z"/></svg>
    <span class="small">CALL OR TEXT NOW</span>
    <span class="num">020-555-0148</span>
  </div>
</header>

<section class="hero" role="img" aria-label="Dark car on a wet road in falling snow beside a stack of winter tires">
  <span class="hero-arrow" style="left:68px">‹</span>
  <span class="hero-arrow" style="left:1116px">›</span>
  <div class="hero-kicker">MOLENVAART</div>
  <h1 class="hero-title">WINTER TIRES</h1>
  <div class="hero-sub">Help Me Find Tires</div>
  <div class="filter-row">
    <div class="filter-select">All Types</div>
    <div class="filter-select">width</div>
    <div class="filter-select">height</div>
    <div class="filter-select">inch</div>
    <div class="filter-btn">SEARCH</div>
  </div>
</section>

<section class="categories">
  <h2>BROWSE BY CATEGORY</h2>
  <div class="cat" style="left:130px"><svg width="60" height="26" viewBox="0 0 60 26" fill="none" stroke="#333" stroke-width="1.5"><path d="M4 18v-5l8-2 8-6h16l10 6 8 2v5H4z"/><circle cx="15" cy="19" r="4" fill="#fff"/><circle cx="45" cy="19" r="4" fill="#fff"/></svg>Car Tire</div>
  <div class="cat" style="left:256px"><svg width="60" height="30" viewBox="0 0 60 30" fill="none" stroke="#333" stroke-width="1.5"><path d="M8 24V4h40l6 10v10z"/><path d="M12 8h30v6H12z"/><circle cx="18" cy="24" r="4" fill="#fff"/><circle cx="44" cy="24" r="4" fill="#fff"/></svg>Van Tire</div>
  <div class="cat" style="left:380px"><svg width="60" height="30" viewBox="0 0 60 30" fill="none" stroke="#333" stroke-width="1.5"><path d="M4 22V4h34v18z"/><path d="M38 10h10l6 7v5H38z"/><circle cx="14" cy="24" r="4" fill="#fff"/><circle cx="46" cy="24" r="4" fill="#fff"/></svg>Truck Tire</div>
  <div class="cat" style="left:501px"><svg width="50" height="30" viewBox="0 0 50 30" fill="none" stroke="#333" stroke-width="1.5"><path d="M6 24V4h38v20z"/><path d="M10 8h30v6H10z"/><circle cx="15" cy="25" r="3" fill="#fff"/><circle cx="35" cy="25" r="3" fill="#fff"/></svg>RVS Tire</div>
  <div class="cat" style="left:641px"><svg width="56" height="30" viewBox="0 0 56 30" fill="none" stroke="#333" stroke-width="1.5"><path d="M4 20l4-14h26l-2 14z"/><path d="M34 10h10l6 7v5H34z"/><circle cx="12" cy="24" r="4" fill="#fff"/><circle cx="24" cy="24" r="4" fill="#fff"/><circle cx="44" cy="24" r="4" fill="#fff"/></svg>Dump Truck Tire</div>
  <div class="cat" style="left:786px"><svg width="60" height="28" viewBox="0 0 60 28" fill="none" stroke="#333" stroke-width="1.5"><path d="M4 20v-6l8-2 6-6h22l8 6 8 2v6z"/><path d="M24 2h10v4H24z"/><circle cx="16" cy="21" r="4" fill="#fff"/><circle cx="44" cy="21" r="4" fill="#fff"/></svg>Taxi Tire</div>
  <div class="cat" style="left:929px"><svg width="50" height="30" viewBox="0 0 50 30" fill="none" stroke="#333" stroke-width="1.5"><path d="M4 24V4h30l12 10v10z"/><path d="M16 9v8M12 13h8"/><circle cx="14" cy="25" r="3" fill="#fff"/><circle cx="38" cy="25" r="3" fill="#fff"/></svg>Ambulance Tire</div>
  <div class="cat" style="left:1069px"><svg width="50" height="30" viewBox="0 0 50 30" fill="none" stroke="#333" stroke-width="1.5"><path d="M4 24V4h42v20z"/><path d="M8 8h34v7H8z"/><circle cx="14" cy="25" r="3" fill="#fff"/><circle cx="36" cy="25" r="3" fill="#fff"/></svg>Bus Tire</div>
</section>

<section class="products">
  <h2 class="heading">OUR WINTER TIRE</h2>
  <p class="lead">Sed ut perspiciatis unde omnis iste natus error sit voluptatem accusantiu</p>

  <div class="product-card" style="left:100px;top:171px"><div class="product-photo" role="img" aria-label="Product photo of a winter tire"></div><div class="rating"><span>★★★★★</span> 125</div><div class="name">The standard Lorem</div><div class="price">$45.00</div><div class="btn">Shop Now</div></div>
  <div class="product-card" style="left:353px;top:171px"><div class="product-photo" role="img" aria-label="Product photo of a winter tire"></div><div class="rating"><span>★★★★★</span> 125</div><div class="name">The standard Lorem</div><div class="price">$45.00</div><div class="btn">Shop Now</div></div>
  <div class="product-card" style="left:607px;top:171px"><div class="product-photo" role="img" aria-label="Product photo of a winter tire"></div><div class="rating"><span>★★★★★</span> 125</div><div class="name">The standard Lorem</div><div class="price">$45.00</div><div class="btn">Shop Now</div></div>
  <div class="product-card" style="left:860px;top:171px"><div class="product-photo" role="img" aria-label="Product photo of a winter tire"></div><div class="rating"><span>★★★★★</span> 125</div><div class="name">The standard Lorem</div><div class="price">$45.00</div><div class="btn">Shop Now</div></div>

  <div class="product-card" style="left:100px;top:493px"><div class="product-photo" role="img" aria-label="Product photo of a winter tire"></div><div class="rating"><span>★★★★★</span> 125</div><div class="name">The standard Lorem</div><div class="price">$45.00</div><div class="btn">Shop Now</div></div>
  <div class="product-card" style="left:353px;top:493px"><div class="product-photo" role="img" aria-label="Product photo of a winter tire"></div><div class="rating"><span>★★★★★</span> 125</div><div class="name">The standard Lorem</div><div class="price">$45.00</div><div class="btn">Shop Now</div></div>
  <div class="product-card" style="left:607px;top:493px"><div class="product-photo" role="img" aria-label="Product photo of a winter tire"></div><div class="rating"><span>★★★★★</span> 125</div><div class="name">The standard Lorem</div><div class="price">$45.00</div><div class="btn">Shop Now</div></div>
  <div class="product-card" style="left:860px;top:493px"><div class="product-photo" role="img" aria-label="Product photo of a winter tire"></div><div class="rating"><span>★★★★★</span> 125</div><div class="name">The standard Lorem</div><div class="price">$45.00</div><div class="btn">Shop Now</div></div>
</section>

<section class="features">
  <div class="dark-panel"></div>
  <h2>TIRE FEATURES &amp; BENEFITS</h2>
  <div class="feature active" style="top:104px"><h3>Competitive Handling</h3><p>Solid ribs increase block stiffness for high-speed stability and superior handling.</p></div>
  <div class="feature" style="top:209px"><h3>Efficient Grip</h3><p>Excellent hydroplaning resistance and shorter stops on wet roads.</p></div>
  <div class="feature" style="top:296px"><h3>Quiet Ride</h3><p>An offset tread pattern increases stability and reduces pattern noise.</p></div>
  <div class="feature" style="top:383px"><h3>Fuel Efficient</h3><p>Nano-blend compound with micro silica reduces rolling resistance.</p></div>
  <div class="feature-visual" role="img" aria-label="Cutaway illustration of a tire showing the outer and center ribs"></div>
  <div class="pointer" style="left:592px;top:183px;width:250px"></div>
  <div class="pointer" style="left:658px;top:308px;width:184px"></div>
  <div class="dot" style="left:578px;top:176px"></div>
  <div class="dot" style="left:645px;top:301px"></div>
  <div class="rib-label" style="top:137px"><h4>SOLID OUTER RIB</h4><p>Increases block stiffness for superior handling.</p></div>
  <div class="rib-label" style="top:260px"><h4>SOLID CENTER RIB</h4><p>Provides high-speed stability and better on-center feel.</p></div>
</section>

<section class="mounting">
  <div class="photo" role="img" aria-label="Mechanic in blue overalls rolling a tire in a workshop"></div>
  <h2 class="heading">OUR MOUNTING SERVICE</h2>
  <p class="lead">Lorem ipsum dolor sit amet, consectetur adipiscing elit, sed do eiusmod tempor incididunt ut labore</p>
  <div class="service" style="left:636px;top:194px"><svg width="36" height="36" viewBox="0 0 36 36" fill="none" stroke="#fff" stroke-width="1.6"><path d="M6 30L24 12M22 6a6 6 0 0 0 8 8l-4-4zM6 6l24 24M4 8l4-4 4 4-4 4z"/></svg><h3>The standard Lorem Ipsum</h3><p>Sed ut perspiciatis unde omnis iste natus error sit voluptatem accusantium</p></div>
  <div class="service" style="left:865px;top:194px"><svg width="36" height="36" viewBox="0 0 36 36" fill="none" stroke="#fff" stroke-width="1.6"><circle cx="18" cy="18" r="15"/><circle cx="18" cy="18" r="9"/><circle cx="18" cy="18" r="3"/></svg><h3>The standard Lorem Ipsum</h3><p>Sed ut perspiciatis unde omnis iste natus error sit voluptatem accusantium</p></div>
  <div class="service" style="left:636px;top:316px"><svg width="36" height="36" viewBox="0 0 36 36" fill="none" stroke="#fff" stroke-width="1.6"><rect x="4" y="8" width="28" height="22" rx="2"/><circle cx="18" cy="19" r="7"/><path d="M10 4h16"/></svg><h3>The standard Lorem Ipsum</h3><p>Sed ut perspiciatis unde omnis iste natus error sit voluptatem accusantium</p></div>
  <div class="service" style="left:865px;top:316px"><svg width="36" height="36" viewBox="0 0 36 36" fill="none" stroke="#fff" stroke-width="1.6"><circle cx="18" cy="18" r="15"/><path d="M18 10v8l5 4"/></svg><h3>The standard Lorem Ipsum</h3><p>Sed ut perspiciatis unde omnis iste natus error sit voluptatem accusantium</p></div>
  <div class="btn-red">LEARN MORE</div>
</section>

<section class="blog">
  <h2 class="heading">LATEST BLOG</h2>
  <article class="post" style="left:110px"><div class="post-photo" role="img" aria-label="Off-road vehicle tire on a snowy forest track" style="background:linear-gradient(160deg,#d9d6d0,#8d8a86 55%,#e6e3de)"></div><h3>The standard Lorem Ipsum passage, use the 1500s</h3><p>Sed ut perspiciatis unde omnis iste natus error sit voluptatem accusantium doloremque laudantium, totam rem aperiam,</p><a>Read More &gt;&gt;</a></article>
  <article class="post" style="left:444px"><div class="post-photo" role="img" aria-label="Mechanic carrying a tire beside a car" style="background:linear-gradient(160deg,#eceff2,#9aa3ad 55%,#2c3e60)"></div><h3>The standard Lorem Ipsum passage, use the 1500s</h3><p>Sed ut perspiciatis unde omnis iste natus error sit voluptatem accusantium doloremque laudantium, totam rem aperiam,</p><a>Read More &gt;&gt;</a></article>
  <article class="post" style="left:778px"><div class="post-photo" role="img" aria-label="Gloved hands lifting a tire in a tire shop" style="background:linear-gradient(110deg,#3a3a3a,#1a1a1a 45%,#c9a030 80%,#a33)"></div><h3>The standard Lorem Ipsum passage, use the 1500s</h3><p>Sed ut perspiciatis unde omnis iste natus error sit voluptatem accusantium doloremque laudantium, totam rem aperiam,</p><a>Read More &gt;&gt;</a></article>
</section>

<section class="newsletter" role="img" aria-label="Tire with chrome rim on a snowy mountain road">
  <h2 class="heading">SIGN FOR NEWSLETTER</h2>
  <p class="lead">Lorem ipsum dolor sit amet, consectetur adipiscing elit, sed do eiusmod tempor incididunt ut labore et</p>
  <div class="subscribe"><span>Enter Email Address</span><b>SUBSCRIBE</b></div>
</section>

<footer class="site-footer">
  <div class="footer-logo">MOLENVAART<span class="mark"></span></div>
  <p class="footer-about">"Sed ut perspiciatinde omnis iste natus error sit voluptatem accusantium doloremque laudantium, totam rem aperiam, eaque ipsa quae ab illo inventore veritatis et quasi architecto beatae vitae dicta sunt explicabo</p>
  <div class="footer-col" style="left:449px"><h4>Site Navigation</h4><ul><li>Home</li><li>What We Do</li><li>About</li><li>Schedule Consultation</li></ul></div>
  <div class="footer-col" style="left:658px"><h4>Contact Us</h4><ul>
    <li><svg width="14" height="16" viewBox="0 0 14 18" fill="#fff"><path d="M7 0a7 7 0 0 1 7 7c0 5-7 11-7 11S0 12 0 7a7 7 0 0 1 7-7zm0 4a3 3 0 1 0 0 6 3 3 0 0 0 0-6z"/></svg><span style="line-height:21px;margin-top:-3px">12 Dijkweg Havenstad<br>4821</span></li>
    <li><svg width="14" height="14" viewBox="0 0 24 24" fill="#fff"><path d="M6.6 10.8a15.1 15.1 0 0 0 6.6 6.6l2.2-2.2a1 1 0 0 1 1-.25 11.4 11.4 0 0 0 3.6.6 1 1 0 0 1 1 1V20a1 1 0 0 1-1 1A17 17 0 0 1 3 4a1 1 0 0 1 1-1h3.5a1 1 0 0 1 1 1c0 1.25.2 2.45.6 3.6a1 1 0 0 1-.25 1z"/></svg>020 -555 -0172</li>
    <li><svg width="16" height="12" viewBox="0 0 16 12" fill="#fff"><path d="M0 0h16v12H0zM1.5 1.5v.5L8 7l6.5-5v-.5z"/></svg>info@molenvaart.com</li></ul></div>
  <div class="footer-col social" style="left:922px"><h4>Follow Vaart Media</h4><ul style="margin-top:14px"><li><span class="ring"></span>Workweb</li><li><span class="ring"></span>Chirpline</li><li><span class="ring"></span>Photofeed</li></ul></div>
  <div class="footer-rule"></div>
  <div class="copyright">Copyright © 2021 Molenvaart. All rights reserved.</div>
</footer>

</body>
</html>
```